plumfable business card

need to upgrade current business card for an online retailer of handmade arts and crafts, please visit plumfable.com.au

need to be artistic professional look

sample layout, contents, logo, are in the attached files

need for 4 people, details for other 2 people to be provided later

```html
<!DOCTYPE html>
<html lang="en">
<head>
<meta charset="utf-8">
<title>PlumFable Business Cards</title>
<link rel="stylesheet" href="https://fonts.googleapis.com/css2?family=Didact+Gothic&family=Dancing+Script&display=swap">
<style>
  :root {
    --page-bg: #ebe7e2;
    --card-paper: #f4f4f4;
    --card-pattern-tone: #ebebeb;
    --brand-red: #d63b3e;
    --ink-dark: #2e2b2b;
    --ink-white: #ffffff;
  }
  * { margin: 0; padding: 0; box-sizing: border-box; }
  html, body { width: 1200px; height: 632px; overflow: hidden; }
  body {
    background: var(--page-bg);
    font-family: "Didact Gothic", sans-serif;
    color: var(--ink-dark);
    position: relative;
  }
  .card {
    position: absolute;
    width: 471px;
    height: 234px;
    box-shadow: 0 2px 6px rgba(0,0,0,0.25);
    overflow: hidden;
  }
  .card--front-a { left: 82px; top: 75px; }
  .card--front-b { left: 82px; top: 330px; }
  .card--back-a { left: 600px; top: 75px; }
  .card--back-b { left: 600px; top: 330px; }

  .paper-texture {
    position: absolute; inset: 0;
    background: linear-gradient(135deg, var(--card-paper), var(--card-pattern-tone));
  }
  .front-identity {
    position: absolute; left: 0; top: 0; width: 220px; height: 100%;
  }
  .brand-name {
    position: absolute; left: 26px; top: 38px;
    font-size: 31px; font-weight: 400; color: var(--brand-red);
    letter-spacing: -0.5px;
  }
  .person-name {
    position: absolute; left: 22px; top: 118px;
    font-size: 19px; color: var(--ink-dark);
  }
  .card--front-b .person-name { left: 41px; top: 127px; }
  .person-role {
    position: absolute; left: 22px; top: 148px;
    font-size: 11.5px; color: var(--brand-red);
  }
  .contact-panel {
    position: absolute; left: 220px; top: 0; right: 0; bottom: 0;
    background: var(--brand-red);
    color: var(--ink-white);
  }
  .contact-list {
    position: absolute; left: 14px; list-style: none;
  }
  .card--front-a .contact-list { top: 116px; }
  .card--front-b .contact-list { top: 104px; }
  .contact-item {
    display: flex; align-items: center; gap: 8px;
    font-size: 16.5px; line-height: 23px; height: 23px;
  }
  .contact-icon { width: 17px; height: 17px; flex: none; }
  .services-line {
    position: absolute; left: 14px; top: 184px;
    font-size: 12px; line-height: 16px;
  }
  .services-line strong { font-weight: 700; }

  .back-content {
    position: absolute; inset: 0; text-align: center;
  }
  .back-headline {
    position: absolute; left: 0; right: 0;
    font-size: 12px; font-weight: 700; line-height: 15px;
  }
  .card--back-a .back-headline { top: 49px; }
  .card--back-b .back-headline { top: 47px; }
  .product-list { position: absolute; left: 0; right: 0; list-style: none; }
  .card--back-a .product-list { top: 86px; font-size: 14.5px; line-height: 18.5px; }
  .card--back-b .product-list { top: 89px; font-size: 14.5px; line-height: 14.5px; }
  .product-list .highlight { color: var(--brand-red); }
  .eco-note {
    position: absolute; left: 0; right: 0;
    font-family: "Dancing Script", cursive;
    font-size: 12.5px;
  }
  .card--back-a .eco-note { top: 198px; }
  .card--back-b .eco-note { top: 194px; }
</style>
</head>
<body>

<svg width="0" height="0" style="position:absolute" aria-hidden="true">
  <defs>
    <symbol id="icon-phone" viewBox="0 0 20 20">
      <circle cx="10" cy="10" r="10" fill="#ffffff"/>
      <path d="M7 5 L8.6 5 L9.4 7.6 L8.3 8.5 C8.9 9.8 10.2 11.1 11.5 11.7 L12.4 10.6 L15 11.4 L15 13 C15 13.8 14.3 14.3 13.5 14.2 C9.5 13.7 6.3 10.5 5.8 6.5 C5.7 5.7 6.2 5 7 5 Z" fill="#d63b3e"/>
    </symbol>
    <symbol id="icon-mail" viewBox="0 0 20 20">
      <circle cx="10" cy="10" r="10" fill="#ffffff"/>
      <rect x="5" y="6.5" width="10" height="7" rx="0.8" fill="#d63b3e"/>
      <path d="M5.3 7 L10 10.6 L14.7 7" fill="none" stroke="#ffffff" stroke-width="1"/>
    </symbol>
    <symbol id="icon-web" viewBox="0 0 20 20">
      <circle cx="10" cy="10" r="10" fill="#ffffff"/>
      <circle cx="10" cy="10" r="5" fill="none" stroke="#d63b3e" stroke-width="1.3"/>
      <ellipse cx="10" cy="10" rx="2.1" ry="5" fill="none" stroke="#d63b3e" stroke-width="1.1"/>
      <line x1="5" y1="10" x2="15" y2="10" stroke="#d63b3e" stroke-width="1.1"/>
    </symbol>
  </defs>
</svg>

<section class="card card--front-a">
  <div class="paper-texture" role="img" aria-label="Faint grey interlocking key pattern across the card"></div>
  <div class="front-identity">
    <div class="brand-name">PlumFable</div>
    <div class="person-name">Milan Rai</div>
    <div class="person-role">Director, PlumFable Australia</div>
  </div>
  <div class="contact-panel" role="img" aria-label="Red panel with subtle tonal key pattern">
    <ul class="contact-list">
      <li class="contact-item"><svg class="contact-icon"><use href="#icon-phone"/></svg>milan@plumfable.com.au</li>
      <li class="contact-item"><svg class="contact-icon"><use href="#icon-mail"/></svg>+61 491 570 156</li>
    </ul>
  </div>
</section>

<section class="card card--front-b">
  <div class="paper-texture" role="img" aria-label="Faint grey interlocking key pattern across the card"></div>
  <div class="front-identity">
    <div class="brand-name">PlumFable</div>
    <div class="person-name">Sujan Karki</div>
  </div>
  <div class="contact-panel" role="img" aria-label="Red panel with subtle tonal key pattern">
    <ul class="contact-list">
      <li class="contact-item"><svg class="contact-icon"><use href="#icon-web"/></svg>www.plumfable.com.au</li>
      <li class="contact-item"><svg class="contact-icon"><use href="#icon-phone"/></svg>sujan@plumfable.com.au</li>
      <li class="contact-item"><svg class="contact-icon"><use href="#icon-mail"/></svg>+61 491 570 110</li>
    </ul>
    <p class="services-line"><strong>We do handicrafts</strong> Design/Promotion<br>Wholesale/Export &nbsp;-&nbsp; Import/Export</p>
  </div>
</section>

<section class="card card--back-a">
  <div class="paper-texture" role="img" aria-label="Faint grey interlocking key pattern across the card"></div>
  <div class="back-content">
    <p class="back-headline">Visit us for exotic hand-made arts &amp; crafts<br>around the globe</p>
    <ul class="product-list">
      <li class="highlight">Cashmere fashion items from Nepal</li>
      <li>Thai Traditional Paintings</li>
      <li>Nepali/Tibeten Thangkas</li>
      <li>Lokta/Rice Paper Crafts</li>
      <li>Allo/Cotton/Woollen Items</li>
    </ul>
    <p class="eco-note">We encourage eco-friendly, sustainable and traditional arts practice</p>
  </div>
</section>

<section class="card card--back-b">
  <div class="paper-texture" role="img" aria-label="Faint grey interlocking key pattern across the card"></div>
  <div class="back-content">
    <p class="back-headline">Visit us for exotic hand-made arts &amp; crafts<br>around the globe</p>
    <ul class="product-list">
      <li>Thai Traditional Paintings</li>
      <li>Nepali/Tibeten Thangkas</li>
      <li>Lokta/Rice Paper Crafts</li>
      <li>Allo/Cotton/Woollen Items</li>
      <li>Fashion/Jewellery</li>
      <li>Other Gift/Decoration Items</li>
    </ul>
    <p class="eco-note">We encourage eco-friendly, sustainable and traditional arts practice</p>
  </div>
</section>

</body>
</html>
```